Website Design for Solar Panel Company

We are working with a company called BrightVX.

Some sites to use for content/competitors and inspiration:
https://www.dawnmill.com
https://prod.cdn-prod.raylokt.com
https://mossbeamvolt.net
https://www.quorvin.com/solarpanels

Thank you for taking the time to consider designing a website for us. We are web developers based in Stockton, CA, USA. Most of our projects go through the same process. Understanding this process may help you win a project with us. We custom-code all of our websites in-house. We don’t have any requirements as to what tools you use for your design, but we prefer Figma files. For any design that we label as four-stars, we send it to the client for review. The client picks the final design they want us to use. Once we complete this process, we will continue to show additional clients all the four-star sites and purchase them later. Your designs will have multiple chances to sell. For better chances of success, we ask that you follow these guidelines.

IMAGES:
If you use any images or icons in the design, we ask that you have a link to the asset so we can purchase the image/icon. Most of the designs we submit do not have the customer’s images on them unless they have some great images. Be creative; show us the feeling you are trying to portray with your image choices. Use any royalty-free site you choose. We subscribe to Corvane and mainly use their images, but we can purchase images outside of Corvane. PLEASE NOTE: we will not submit designs to clients with watermarks on the images.

FONTS:
We ask that you identify the fonts used in the design. This can be done in a message if you want. We typically use Tivelo Fonts and Corvane Fonts.

CONTENT:
We're always open to different content and ideas. We often submit designs with stock images so the client can see our vision. We typically take pictures after the website launch to use their images with our vision. Lorem Ipsum is fine for paragraphs, but we ask that you write the headers in correct English. We want to be able to show the vision and identify the sections of the website.

INSPIRATION:
We typically add a couple of links in the brief of websites we like to help you get started in your design.

REVISIONS:
We do not often ask for revisions of the designs unless we see something in the design that may not appeal to the client. If there are slight changes that we want to make, we do that in the development process.

FEEDBACK:
We rarely give feedback on designs during the design process. We are working on many website projects and do not have the time to provide feedback. We usually respond if your request is well thought out and asks specific questions, but a note asking “feedback, please” usually goes unanswered.

```html
<!DOCTYPE html>
<html lang="en">
<head>
<meta charset="utf-8">
<title>BrightVX – Solar Energy</title>
<link href="https://fonts.googleapis.com/css2?family=Open+Sans:wght@400;600;700;800&display=swap" rel="stylesheet">
<style>
:root{
  --navy:#0e2b5e;
  --navy-dark:#0a1526;
  --green:#6cc01f;
  --green-dark:#4f9a12;
  --ink:#2b3340;
  --muted:#6b7480;
  --light:#f2f4f7;
  --white:#ffffff;
  --line:#dfe3e8;
}
*{margin:0;padding:0;box-sizing:border-box}
html,body{width:1200px;height:4692px;overflow:hidden}
body{font-family:"Open Sans",Arial,sans-serif;color:var(--ink);background:var(--white);position:relative}
.abs{position:absolute}
section,header,footer{position:absolute;left:0;width:1200px;overflow:hidden}
.label{font-size:13px;font-weight:700;color:var(--green);letter-spacing:1px;text-transform:uppercase}
.label.center{text-align:center}
.title{font-weight:700;color:var(--navy);text-align:center}
.btn{display:inline-block;background:var(--green);color:#fff;font-weight:700;font-size:16px;border-radius:6px;padding:12px 28px}
p.lorem{font-size:15px;line-height:24px;color:var(--muted)}

/* Hero */
.hero{top:0;height:880px;background:linear-gradient(180deg,#1b1f2a 0%,#3a2a22 30%,#8a5626 55%,#b7742f 68%,#3b3f4a 85%,#22262e 100%)}
.hero-photo{position:absolute;inset:0}
.topbar{position:absolute;top:0;left:0;width:1200px;height:48px;display:flex;align-items:center;padding:0 128px;color:#dfe6f0;font-size:14px;gap:36px}
.topbar .social{margin-left:auto;display:flex;gap:14px}
.topbar .social span{width:14px;height:14px;border-radius:50%;background:#cfd8e6}
.brand{position:absolute;left:128px;top:54px;font-size:34px;font-weight:800;color:#fff;letter-spacing:.5px}
.badges{position:absolute;top:62px;left:840px;display:flex;gap:70px;color:#fff;font-size:14px;font-weight:700;line-height:18px}
.nav{position:absolute;left:128px;top:128px;width:944px;height:68px;background:#fff;border-radius:6px;display:flex;align-items:center;padding:0 48px;gap:62px;font-size:16px;font-weight:600;color:var(--navy)}
.nav .active{position:relative;color:var(--navy);font-weight:700}
.nav .active::after{content:"";position:absolute;left:-6px;right:-6px;bottom:-22px;height:4px;background:var(--green)}
.nav .btn{margin-left:auto;font-size:14px;padding:10px 26px;border-radius:20px}
.hero-copy{position:absolute;top:380px;width:1200px;text-align:center;color:#fff}
.hero-copy .welcome{font-size:16px;margin-bottom:18px}
.hero-copy h1{font-size:58px;font-weight:600;line-height:74px;letter-spacing:1px}
.hero-copy .btn{margin-top:42px;border-radius:20px;font-size:15px;padding:10px 30px}
.hero-curve{position:absolute;left:0;bottom:0}

/* About */
.about{top:880px;height:560px}
.about-photo{position:absolute;left:80px;top:56px;width:460px;height:460px;border-radius:50%;border:10px solid var(--navy);background:linear-gradient(160deg,#9db4c8 0%,#6e7e88 45%,#36424f 100%)}
.about-badge{position:absolute;left:430px;top:396px;width:96px;height:96px;border-radius:50%;background:#fff;display:flex;align-items:center;justify-content:center}
.about-badge span{width:72px;height:72px;border-radius:50%;background:var(--green)}
.about-text{position:absolute;left:608px;top:84px;width:520px}
.about-text h2{font-size:40px;line-height:50px;color:var(--navy);font-weight:700;margin:10px 0 20px}
.about-text h3{font-size:20px;color:var(--green-dark);font-weight:600;margin-bottom:16px}
.about-text p{margin-bottom:18px}
.about-text .btn{margin-top:10px;border-radius:4px;font-size:15px;padding:9px 24px}

/* Services */
.services{top:1440px;height:540px;background:var(--light)}
.services .label{margin-top:54px}
.services .title{font-size:46px;margin-top:10px}
.cards{position:absolute;top:188px;left:100px;display:flex;gap:32px}
.card{width:312px;height:312px;background:#fff;text-align:center;padding:60px 28px 0;position:relative}
.card.featured{background:linear-gradient(180deg,#5f5a56 0%,#35373d 100%);color:#fff;border-bottom:6px solid var(--green)}
.card svg{display:block;margin:0 auto 16px}
.card h4{font-size:20px;font-weight:600;color:var(--navy);margin-bottom:18px}
.card.featured h4{color:#fff}
.card p{font-size:15px;line-height:22px;color:var(--muted)}
.card.featured p{color:#eee}

/* CTA */
.cta{top:1980px;height:340px;background:linear-gradient(180deg,#0d1420 0%,#17202f 60%,#0c121c 100%)}
.cta h2{position:absolute;top:112px;width:1200px;text-align:center;color:#fff;font-size:38px;font-weight:600;line-height:52px}
.cta h2 em{font-style:normal;color:var(--green)}
.cta-bar{position:absolute;left:352px;top:288px;width:500px;height:52px;background:#fff;border-radius:4px;display:flex;align-items:center;justify-content:space-around;font-size:16px;font-weight:600;color:var(--navy)}

/* Why */
.why{top:2320px;height:640px}
.why .label{margin-top:66px}
.why .title{font-size:46px;margin-top:8px}
.why-grid{position:absolute;top:188px;left:120px;width:952px;height:424px}
.why-grid div{position:absolute}

/* Testimonials */
.testimonials{top:2960px;height:640px;background:linear-gradient(180deg,#0f1826 0%,#1b2433 50%,#0d141f 100%)}
.testimonials .label{margin-top:52px;color:#fff;display:block;width:120px;margin-left:540px;text-align:center;border-bottom:2px solid #fff;padding-bottom:4px}
.testimonials .title{color:#fff;font-size:44px;margin-top:12px}
.tcards{position:absolute;top:180px;left:100px;display:flex;gap:32px}
.tcard{width:312px;height:420px;background:var(--navy);border:2px solid #2e5aa0;text-align:center;padding:30px 26px 0;color:#d8e1f0;position:relative}
.tcard.light{background:#fff;border:none;border-bottom:8px solid var(--green);color:var(--muted)}
.avatar{width:76px;height:76px;border-radius:50%;margin:0 auto 14px;background:linear-gradient(180deg,#8d96a2,#4b5360);border:3px solid #fff}
.tcard h5{font-size:20px;font-weight:600;color:#fff}
.tcard.light h5{color:var(--navy)}
.stars{color:#ff6a2b;font-size:20px;letter-spacing:3px;margin:6px 0 22px}
.tcard p{font-size:15px;line-height:23px}
.quote{position:absolute;left:0;right:0;bottom:34px;font-size:60px;line-height:40px;color:var(--green);font-weight:800}
.dots{position:absolute;top:614px;left:0;width:1200px;display:flex;justify-content:center;gap:10px}
.dots span{width:10px;height:10px;border-radius:50%;background:#5a6372}
.dots span.on{background:#fff}

/* Contact */
.contact{top:3600px;height:680px}
.contact h2{position:absolute;left:100px;top:56px;font-size:46px;color:var(--navy);font-weight:600}
.contact h2 span{font-weight:400}
.info{position:absolute;left:118px;top:150px}
.info-item{display:flex;gap:26px;margin-bottom:44px;align-items:flex-start}
.info-item svg{flex:none}
.info-item b{display:block;font-size:14px;color:var(--navy);margin-bottom:4px}
.info-item span{font-size:14px;color:var(--muted)}
.form{position:absolute;left:600px;top:40px;width:500px;height:580px;background:#fff;border-top:6px solid var(--green);box-shadow:0 6px 30px rgba(0,0,0,.12);padding:36px 36px;z-index:2}
.form h3{font-size:28px;color:var(--navy);font-weight:600;margin-bottom:36px}
.row{display:flex;gap:22px}
.field{flex:1;margin-bottom:24px}
.field label{display:block;font-size:14px;font-weight:600;color:var(--navy);margin-bottom:8px}
.field div{height:46px;border:1px solid var(--line);border-radius:24px;font-size:13px;color:#9aa2ad;padding:13px 18px}
.field div.area{height:132px;border-radius:8px}
.form .btn{font-size:15px;padding:10px 28px;border-radius:4px}
.contact-curve{position:absolute;left:0;top:500px}

/* Footer */
.footer{top:4240px;height:452px;background:var(--navy-dark);color:#c7ceda}
.footer .brand{top:32px;font-size:32px}
.footer-about{position:absolute;left:128px;top:96px;width:280px;font-size:14px;line-height:22px}
.squares{position:absolute;left:128px;top:178px;display:flex;gap:10px}
.squares span{width:26px;height:26px;background:var(--green)}
.fcol{position:absolute;top:40px;font-size:14px;line-height:26px}
.fcol h6{font-size:17px;color:#fff;font-weight:700;margin-bottom:18px}
.news{position:absolute;left:828px;top:40px;width:260px;font-size:14px;line-height:22px}
.news h6{font-size:17px;color:#fff;font-weight:700;margin-bottom:18px}
.news .input{margin-top:22px;display:flex;height:48px}
.news .input div{flex:1;background:#fff;color:#9aa2ad;font-size:13px;padding:15px 14px}
.news .input span{width:48px;background:var(--green);display:flex;align-items:center;justify-content:center}
.fstrip{position:absolute;left:100px;top:260px;width:1000px;display:flex;justify-content:space-between;border-top:1px solid #1f2c44;border-bottom:1px solid #1f2c44;padding:36px 30px}
.fitem{display:flex;gap:16px;align-items:center}
.fitem b{display:block;color:#fff;font-size:16px}
.fitem span{font-size:13px}
.copy{position:absolute;top:412px;width:1200px;text-align:center;color:var(--green);font-size:14px;font-weight:600}
</style>
</head>
<body>

<header class="hero">
  <div class="hero-photo" role="img" aria-label="Photo of solar panels at sunset with warm sky"></div>
  <div class="topbar">
    <span>(+1) 234-567-890</span><span>info@company.com</span><span>123-456-7890</span>
    <div class="social"><span></span><span></span><span></span><span></span></div>
  </div>
  <div class="brand">BrightVX</div>
  <div class="badges"><div>24/7<br>Service</div><div>Qualified<br>Professionals</div></div>
  <nav class="nav">
    <span class="active">Home</span><span>About Us</span><span>Services</span><span>Gallery</span><span>Team</span><span>Contact Us</span>
    <span class="btn">Get A Quote</span>
  </nav>
  <div class="hero-copy">
    <div class="welcome">Welcome</div>
    <h1>For a sustainable<br>tomorrow</h1>
    <span class="btn">About Us</span>
  </div>
  <svg class="hero-curve" width="1200" height="200" viewBox="0 0 1200 200">
    <path d="M0 70 Q600 230 1200 40 L1200 200 L0 200Z" fill="#fff"/>
    <path d="M0 70 Q600 230 1200 40 L1200 78 Q600 250 0 96Z" fill="#6cc01f"/>
    <path d="M0 96 Q600 250 1200 78 L1200 200 L0 200Z" fill="#fff"/>
  </svg>
</header>

<section class="about">
  <div class="about-photo" role="img" aria-label="Photo of a couple looking at rooftop solar panels"></div>
  <div class="about-badge"><span></span></div>
  <div class="about-text">
    <div class="label">Who we are</div>
    <h2>Harnessing solar energy for a cleaner tomorrow</h2>
    <h3>Join the solar movement, make a difference</h3>
    <p class="lorem">Lorem ipsum dolor sit amet, consectetur adipiscing elit, sed do eiusmod tempor incididunt ut labore et dolore magna aliqua. Ut enim ad minim veniam, quis nostrud exercitation ullamco laboris nisi ut aliquip ex ea commodo consequat.</p>
    <p class="lorem">Lorem ipsum dolor sit amet, consectetur adipiscing elit, sed do eiusmod tempor incididunt ut labore et dolore magna aliqua.</p>
    <span class="btn">Contact us &nbsp;→</span>
  </div>
</section>

<section class="services">
  <div class="label center">Our services</div>
  <h2 class="title">Services We Offer</h2>
  <div class="cards">
    <div class="card featured" role="img" aria-label="Photo of a house with installed solar panels">
      <svg width="44" height="44" viewBox="0 0 44 44" fill="none" stroke="#fff" stroke-width="2"><path d="M22 4l5 12 13 1-10 8 3 13-11-7-11 7 3-13L4 17l13-1z"/></svg>
      <h4>Panel Installation</h4>
      <p>Lorem ipsum dolor sit amet, consectetur adipiscing elit, sed do eiusmod tempor</p>
    </div>
    <div class="card">
      <svg width="44" height="44" viewBox="0 0 44 44" fill="none" stroke="#6cc01f" stroke-width="2"><rect x="6" y="8" width="32" height="24" rx="2"/><path d="M14 38h16M22 32v6M12 24l7-7 5 5 8-8"/></svg>
      <h4>Site Assessment</h4>
      <p>Lorem ipsum dolor sit amet, consectetur adipiscing elit, sed do eiusmod tempor</p>
    </div>
    <div class="card">
      <svg width="44" height="44" viewBox="0 0 44 44" fill="none" stroke="#6cc01f" stroke-width="2"><circle cx="22" cy="12" r="5"/><circle cx="10" cy="30" r="5"/><circle cx="34" cy="30" r="5"/><path d="M18 16l-5 10M26 16l5 10M15 30h14"/></svg>
      <h4>Battery Backup</h4>
      <p>Lorem ipsum dolor sit amet, consectetur adipiscing elit, sed do eiusmod tempor</p>
    </div>
  </div>
</section>

<section class="cta" role="img" aria-label="Dark photo of solar panels">
  <h2>We're On <em>Call 24/7</em> to React Promptly to Your<br>Solar Panel Needs</h2>
  <div class="cta-bar"><span>+ (001) 234-567-890</span><span>(or)</span><span>info@example.com</span></div>
</section>

<section class="why">
  <div class="label center">Why choose us</div>
  <h2 class="title">Why Choose Us</h2>
  <div class="why-grid">
    <div style="left:0;top:0;width:300px;height:424px;background:linear-gradient(160deg,#d7dfe6,#9a8a72 60%,#5a4a3a)" role="img" aria-label="Photo of a technician beside solar panels"></div>
    <div style="left:324px;top:0;width:304px;height:204px;background:linear-gradient(180deg,#7fb5e8,#2f5f9c 60%,#1b3762)" role="img" aria-label="Photo of workers installing solar panels"></div>
    <div style="left:648px;top:0;width:304px;height:204px;background:linear-gradient(160deg,#8a7360,#3c4e66 55%,#253447)" role="img" aria-label="Photo of solar panels on a tiled roof"></div>
    <div style="left:324px;top:220px;width:304px;height:204px;background:radial-gradient(circle at 50% 55%,#fff3c0 0%,#f29a2e 22%,#26476e 60%,#132640)" role="img" aria-label="Photo of sun shining over solar panels"></div>
    <div style="left:648px;top:220px;width:304px;height:204px;background:linear-gradient(160deg,#c7d7e6,#4b6f93 55%,#8a6a4e)" role="img" aria-label="Photo of rooftop solar array"></div>
  </div>
</section>

<section class="testimonials" role="img" aria-label="Dark photo of a city skyline at dusk">
  <div class="label">Testimonials</div>
  <h2 class="title">What Clients are saying</h2>
  <div class="tcards">
    <div class="tcard light">
      <div class="avatar"></div><h5>Thomas Smith</h5><div class="stars">★★★★★</div>
      <p>Lorem ipsum dolor sit amet, consectetur adipiscing elit, sed do eiusmod tempor incididunt ut labore et dolore magna aliqua.</p>
      <div class="quote">“</div>
    </div>
    <div class="tcard">
      <div class="avatar"></div><h5>Jane Doe</h5><div class="stars">★★★★★</div>
      <p>Lorem ipsum dolor sit amet, consectetur adipiscing elit, sed do eiusmod tempor incididunt ut labore et dolore magna aliqua.</p>
      <div class="quote">“</div>
    </div>
    <div class="tcard">
      <div class="avatar"></div><h5>Tom Anand</h5><div class="stars">★★★★★</div>
      <p>Lorem ipsum dolor sit amet, consectetur adipiscing elit, sed do eiusmod tempor incididunt ut labore et dolore magna aliqua.</p>
      <div class="quote">“</div>
    </div>
  </div>
  <div class="dots"><span class="on"></span><span></span><span></span></div>
</section>

<section class="contact">
  <h2>Contact Us <span>Today</span></h2>
  <div class="info">
    <div class="info-item">
      <svg width="44" height="44" viewBox="0 0 44 44" fill="none" stroke="#6cc01f" stroke-width="2"><path d="M8 20L22 8l14 12v16H8z"/><path d="M18 36V26h8v10"/></svg>
      <div><b>HEAD OFFICE</b><span>21 Lorem Street, NY 123</span></div>
    </div>
    <div class="info-item">
      <svg width="44" height="44" viewBox="0 0 44 44" fill="none" stroke="#6cc01f" stroke-width="2"><rect x="6" y="11" width="32" height="22" rx="2"/><path d="M6 13l16 12 16-12"/></svg>
      <div><b>EMAIL ADDRESS</b><span>name@company.com</span></div>
    </div>
    <div class="info-item">
      <svg width="44" height="44" viewBox="0 0 44 44" fill="none" stroke="#6cc01f" stroke-width="2"><path d="M12 6h7l3 9-5 3a22 22 0 0 0 9 9l3-5 9 3v7c0 2-2 4-4 4C21 42 2 23 8 10c0-2 2-4 4-4z"/></svg>
      <div><b>CALL US NOW</b><span>Call Now: 123-456-789</span></div>
    </div>
  </div>
  <svg class="contact-curve" width="1200" height="180" viewBox="0 0 1200 180">
    <path d="M0 150 Q300 20 700 90 L700 180 L0 180Z" fill="#6cc01f"/>
    <path d="M0 170 Q320 50 760 110 Q1000 140 1200 110 L1200 180 L0 180Z" fill="#0a1526"/>
  </svg>
  <div class="form">
    <h3>Send Us A Message</h3>
    <div class="row">
      <div class="field"><label>First Name</label><div>John</div></div>
      <div class="field"><label>Last Name</label><div>Doe</div></div>
    </div>
    <div class="field"><label>Email</label><div>info@company.com</div></div>
    <div class="field"><label>Message</label><div class="area">Type Your Message</div></div>
    <span class="btn">Contact us &nbsp;→</span>
  </div>
</section>

<footer class="footer">
  <div class="brand">BrightVX</div>
  <p class="footer-about">Lorem ipsum dolor sit amet, consectetur adipiscing elit, sed do eiusmod tempor incididunt ut</p>
  <div class="squares"><span></span><span></span><span></span><span></span></div>
  <div class="fcol" style="left:490px"><h6>Quick Links</h6>Home<br>Services<br>About Us<br>Contact<br>Blog<br>Testimonials</div>
  <div class="fcol" style="left:630px;top:84px">Cookies Policy<br>Terms of Use<br>Careers<br>Our Team<br>More</div>
  <div class="news"><h6>Newsletters</h6>Lorem ipsum dolor sit amet, consectetur adipiscing elit
    <div class="input"><div>Enter Email Address</div><span><svg width="16" height="16" viewBox="0 0 16 16"><path d="M3 8h10M9 4l4 4-4 4" stroke="#fff" stroke-width="2" fill="none"/></svg></span></div>
  </div>
  <div class="fstrip">
    <div class="fitem"><svg width="40" height="40" viewBox="0 0 40 40"><circle cx="20" cy="20" r="20" fill="#1f2c44"/><path d="M20 11a6 6 0 0 0-6 6c0 5 6 12 6 12s6-7 6-12a6 6 0 0 0-6-6z" fill="#6cc01f"/></svg><div><b>Address</b><span>123 Middle Road</span></div></div>
    <div class="fitem"><svg width="40" height="40" viewBox="0 0 40 40"><circle cx="20" cy="20" r="20" fill="#6cc01f"/><rect x="11" y="14" width="18" height="12" fill="none" stroke="#fff" stroke-width="2"/><path d="M11 15l9 7 9-7" fill="none" stroke="#fff" stroke-width="2"/></svg><div><b>Email Us</b><span>support@example.com</span></div></div>
    <div class="fitem"><svg width="40" height="40" viewBox="0 0 40 40"><circle cx="20" cy="20" r="20" fill="#1f2c44"/><path d="M14 11h4l2 5-3 2a11 11 0 0 0 5 5l2-3 5 2v4c0 1-1 2-2 2-9 0-16-7-16-15 0-1 1-2 3-2z" fill="#6cc01f"/></svg><div><b>Contact Us</b><span>(+1) (234) 789 89</span></div></div>
    <div class="fitem"><svg width="40" height="40" viewBox="0 0 40 40"><circle cx="20" cy="20" r="20" fill="#1f2c44"/><circle cx="20" cy="20" r="9" fill="none" stroke="#6cc01f" stroke-width="2"/><path d="M20 15v5l3 3" stroke="#6cc01f" stroke-width="2" fill="none"/></svg><div><b>Opening Hour</b><span>Mon - Friday: 10 am - 8pm</span></div></div>
  </div>
  <div class="copy">BrightVX</div>
</footer>

</body>
</html>
```